Creative & Professional Business Card for hair salon

We are looking to update our business cards. Our salon is creative, modern, progressive and professional and looking for a design that will reflect this.

```html
<!DOCTYPE html>
<html lang="en">
<head>
<meta charset="utf-8">
<title>Crowns in the Mist – Business Card</title>
<link href="https://fonts.googleapis.com/css2?family=Josefin+Sans:wght@300&family=Montserrat:wght@500&family=Dancing+Script:wght@400&display=swap" rel="stylesheet">
<style>
  :root {
    --backdrop: #e5e7e9;
    --card: #ffffff;
    --slate: #4d6f85;
    --teal: #6a9aa8;
    --mist: #dfe5e7;
  }
  html, body {
    margin: 0;
    width: 1200px;
    height: 1000px;
    overflow: hidden;
    background: var(--backdrop);
  }
  .canvas { position: relative; width: 1200px; height: 1000px; }
  .card {
    position: absolute;
    left: 278px;
    width: 644px;
    height: 393px;
    background: var(--card);
    overflow: hidden;
  }
  .card--front { top: 75px; }
  .card--back { top: 532px; }

  .front-decor { position: absolute; right: -120px; top: 20px; }

  .brand {
    position: absolute;
    left: 0; right: 0;
    top: 178px;
    text-align: center;
  }
  .brand__name {
    display: inline-flex;
    align-items: center;
    gap: 12px;
    font-family: "Josefin Sans", sans-serif;
    font-weight: 300;
    font-size: 33px;
    color: var(--slate);
    letter-spacing: 0.2px;
  }
  .brand__dot {
    width: 14px; height: 14px;
    border-radius: 50%;
    background: var(--teal);
  }
  .brand__byline {
    margin-top: 8px;
    font-family: "Dancing Script", cursive;
    font-size: 20px;
    color: var(--teal);
    padding-left: 120px;
  }

  .back-dot {
    position: absolute;
    left: 307px; top: 54px;
    width: 30px; height: 30px;
    border-radius: 50%;
    background: var(--mist);
  }
  .appointment-title {
    position: absolute;
    left: 0; right: 0;
    top: 105px;
    text-align: center;
    font-family: "Dancing Script", cursive;
    font-size: 28px;
    color: var(--slate);
    margin: 0;
    font-weight: 400;
  }
  .appointment-line {
    position: absolute;
    left: 28px; right: 28px;
    top: 233px;
    border-top: 1px solid var(--slate);
  }
  .field-label {
    position: absolute;
    top: 238px;
    font-family: "Montserrat", sans-serif;
    font-weight: 500;
    font-size: 14px;
    color: var(--slate);
    letter-spacing: 0.3px;
  }
  .field-label--date { left: 28px; }
  .field-label--time { left: 349px; }

  .contact {
    position: absolute;
    left: 0; right: 0;
    top: 305px;
    text-align: center;
    font-family: "Montserrat", sans-serif;
    font-weight: 500;
    font-size: 15px;
    line-height: 21.5px;
    color: var(--slate);
  }
  .contact p { margin: 0; }
  .sep { padding: 0 8px; }
</style>
</head>
<body>
<div class="canvas">
  <section class="card card--front">
    <svg class="front-decor" width="420" height="420" viewBox="0 0 420 420" aria-hidden="true">
      <circle cx="210" cy="210" r="200" fill="var(--mist)" opacity="0.6"/>
    </svg>
    <div class="brand">
      <div class="brand__name"><span class="brand__dot"></span>Crowns in the Mist</div>
      <div class="brand__byline">by Tess Marlowe</div>
    </div>
  </section>

  <section class="card card--back">
    <div class="back-dot" aria-hidden="true"></div>
    <h2 class="appointment-title">Your next appointment</h2>
    <div class="appointment-line"></div>
    <span class="field-label field-label--date">DATE</span>
    <span class="field-label field-label--time">TIME</span>
    <div class="contact">
      <p>5/12 Harlow Lane, Kenmore<span class="sep">|</span>Ph: 07 5123 4098</p>
      <p>E: hello@crownsinthemist.com.au<span class="sep">|</span>www.crownsinthemist.com.au</p>
      <p>Social: @CrownsInTheMistByTessMarlowe</p>
    </div>
  </section>
</div>
</body>
</html>
```